Verpackungen für Trinkflasche
Zielgruppe
Wir produzieren Outdoor Artikel.
Aufgabenstellung
Es soll eine Verpackung für eine vakuumisolierte, doppelwandige Wasserflasche & Trinkflasche aus Hochwertigem Edelstahl designed werden. Die Flasche soll abgebildet sein, am besten halb offen (das Innere ist zu sehen) und halb geschlossen (das Äußere ist zu sehen). Die Besonderheiten und Eigenschaften sollen dann jeweils durch Pfeile möglichst modern /futuristisch kenntlich gemacht werden. Ich habe dafür Beispielbilder angehängt.
Die Besonderheiten:
Edelstahl
BPA-frei
doppelwandige Vakuumtechnologie
hält Getränke 24 h kalt
hält Getränke 12 h heiss
auslaufsicher
Flaschenhalterung inkl. Karabiner enthalten
500 mL
Titel auf der Verpackung in etwa so:
Trinkflasche
Outdoor / Sport / Abenteuer
Es muss Platz bleiben für einen ca. 4 x 2 cm großen Barcode (gibt es dann für den Gewinner zum Schluss des PRojektes zum Einfügen).
Die Trinkflasche wird es in 3 Farben geben: Blau, Schwarz, Grau
Zunächst bitte das Design für die blaue Flasche erstellen... das Gewinner-Design sollte dann noch auf die schwarze und graue angepasst werden.
Zusätzlich sollte jeweils ein 3D Mockup erstellt werden.
Zu den angehängten Bildern:
Es sind jeweils Beispielbilder der Farben gezeigt. Zusätzlich sind Design Beispiele gezeigt, wie ich mir ungefähr die Darstellung der Flaschen auf der Verpackung vorstelle.
Professionelle Fotos der Flaschen gibt es noch nicht. Hier bitte selbst aktiv werden oder bei z.B. Marktora umschauen (Beispiel: https://www.marktora.example/KELP-Flask-Vakuumisolierte-Doppelwandige-Isolierflasche/dp/Q07T3ZR4XD/ref=pd_cp_200_2?_encoding=UTF8&refRID=WQPLNHSAVD8EYTMBRXUC )
Der enthaltene Flaschenhalter ist ebenfalls gezeigt auf den Fotos, ich denke hier reicht eine schemenhafte Darstellung.
Fragen? Einfach stellen ;)

```html
<!DOCTYPE html>
<html lang="de">
<head>
<meta charset="utf-8">
<title>Trailwerk Thermo Trinkflasche – Verpackung</title>
<link rel="stylesheet" href="https://fonts.googleapis.com/css2?family=Exo+2:wght@400;500;700&display=swap">
<style>
  :root {
    --stage: #eeeeee;
    --panel-top: #fbfbfb;
    --panel-mid: #d8dccb;
    --panel-bottom: #7f9a52;
    --brand-green: #6e9a2c;
    --ring-green: #7aa33a;
    --text-dark: #2b2b2b;
    --text-white: #ffffff;
    --icon-grey: #9a9a9a;
    --bottle-blue: #1d3f8a;
    --bottle-grey: #6b6f74;
  }
  * { box-sizing: border-box; margin: 0; padding: 0; }
  html, body { width: 1200px; height: 1200px; overflow: hidden; }
  body {
    background: var(--stage);
    font-family: "Exo 2", sans-serif;
    color: var(--text-dark);
    display: flex;
    justify-content: center;
    align-items: center;
    gap: 16px;
  }
  .panel {
    position: relative;
    width: 400px;
    height: 1100px;
    background: linear-gradient(180deg, var(--panel-top) 0%, var(--panel-top) 30%, var(--panel-mid) 62%, var(--panel-bottom) 100%);
    box-shadow: 0 4px 16px rgba(0,0,0,0.15);
  }

  /* Side panel */
  .brand {
    position: absolute; top: 150px; left: 0; right: 0;
    display: flex; align-items: center; justify-content: center; gap: 14px;
  }
  .brand-dot { width: 26px; height: 26px; border-radius: 50%; background: var(--brand-green); }
  .brand-name { font-size: 44px; font-weight: 700; color: var(--brand-green); letter-spacing: 2px; }

  .feature-list {
    position: absolute; top: 470px; left: 40px; right: 30px;
    list-style: none;
  }
  .feature-list li {
    position: relative;
    padding-left: 40px;
    font-size: 19px; line-height: 1.4;
    margin-bottom: 24px;
  }
  .feature-list li::before {
    content: "";
    position: absolute; left: 6px; top: 8px;
    width: 11px; height: 11px;
    background: var(--ring-green);
    border: 2px solid var(--text-dark);
    transform: rotate(45deg);
  }

  /* Front panel */
  .tagline {
    position: absolute; top: 22px; left: 0; right: 0;
    text-align: center; font-size: 16px; font-weight: 500; color: var(--brand-green);
  }
  .icon-column { position: absolute; top: 120px; left: 22px; width: 96px; }
  .icon-item { text-align: center; margin-bottom: 26px; }
  .icon-item svg { display: block; width: 90px; height: 90px; margin: 0 auto; }
  .icon-label { font-size: 22px; font-weight: 500; margin-top: 8px; }

  .bottle-visual {
    position: absolute; top: 60px; left: 150px; width: 220px; height: 640px;
    border-radius: 60px 60px 24px 24px;
    background: linear-gradient(90deg, var(--bottle-blue) 0%, #3a64c0 40%, var(--bottle-blue) 60%, var(--bottle-grey) 85%, #a8acb0 100%);
  }
  .detail-connectors { position: absolute; top: 660px; left: 0; width: 400px; height: 120px; }
  .detail-ring {
    position: absolute; top: 745px; width: 100px; height: 100px; border-radius: 50%;
    border: 6px solid var(--ring-green);
  }
  .detail-ring.cap { left: 88px; background: radial-gradient(circle, #d0d2d4, #7c8084); }
  .detail-ring.inside { left: 218px; background: linear-gradient(90deg, #5a5e63, #c9e6ee 55%, #8a8e92); }

  .product-title {
    position: absolute; top: 880px; left: 0; right: 0; text-align: center;
  }
  .product-title .thermo { font-size: 64px; font-weight: 700; color: #111; line-height: 1; letter-spacing: 1px; }
  .product-title .kind { font-size: 40px; font-weight: 500; color: var(--text-white); line-height: 1.15; }
  .volume {
    position: absolute; bottom: 40px; left: 0; right: 0; text-align: center;
    font-size: 20px; font-weight: 500;
  }
</style>
</head>
<body>

  <section class="panel panel-side">
    <div class="brand">
      <span class="brand-dot"></span>
      <span class="brand-name">TRAILWERK</span>
    </div>
    <ul class="feature-list">
      <li>Edelstahl</li>
      <li>BPA-frei</li>
      <li>doppelwandige<br>Vakuumtechnologie</li>
      <li>hält Getränke<br>24 h kalt</li>
      <li>hält Getränke<br>12 h heiss</li>
      <li>auslaufsicher</li>
      <li>Flaschenhalterung<br>inkl. Karabiner<br>enthalten</li>
      <li>500 mL</li>
    </ul>
  </section>

  <section class="panel panel-front">
    <p class="tagline">Outdoor / Sport / Abenteuer</p>

    <div class="bottle-visual" role="img" aria-label="Produktfoto: blaue und graue Edelstahl-Trinkflasche nebeneinander"></div>

    <div class="icon-column">
      <div class="icon-item">
        <svg viewBox="0 0 90 90" aria-label="auslaufsicher">
          <circle cx="45" cy="45" r="40" fill="#f2f2f2" stroke="var(--ring-green)" stroke-width="6"/>
          <path d="M40 28 C34 38 30 44 30 50 a10 10 0 0 0 20 0 C50 44 46 38 40 28Z" fill="#4aa3d8"/>
          <path d="M56 40 C53 45 51 48 51 51 a5 5 0 0 0 10 0 C61 48 59 45 56 40Z" fill="#4aa3d8"/>
          <line x1="22" y1="22" x2="68" y2="68" stroke="var(--icon-grey)" stroke-width="7"/>
        </svg>
      </div>
      <div class="icon-item">
        <svg viewBox="0 0 90 90" aria-label="kalt">
          <circle cx="45" cy="45" r="40" fill="#f2f2f2" stroke="var(--ring-green)" stroke-width="6"/>
          <g stroke="#3d8fd6" stroke-width="4" stroke-linecap="round">
            <line x1="45" y1="27" x2="45" y2="63"/>
            <line x1="29" y1="36" x2="61" y2="54"/>
            <line x1="29" y1="54" x2="61" y2="36"/>
          </g>
        </svg>
        <div class="icon-label">24h</div>
      </div>
      <div class="icon-item">
        <svg viewBox="0 0 90 90" aria-label="heiss">
          <circle cx="45" cy="45" r="40" fill="#f2f2f2" stroke="var(--ring-green)" stroke-width="6"/>
          <circle cx="45" cy="45" r="9" fill="#e2561e"/>
          <g stroke="#e2561e" stroke-width="3" stroke-linecap="round">
            <line x1="45" y1="25" x2="45" y2="31"/><line x1="45" y1="59" x2="45" y2="65"/>
            <line x1="25" y1="45" x2="31" y2="45"/><line x1="59" y1="45" x2="65" y2="45"/>
            <line x1="31" y1="31" x2="35" y2="35"/><line x1="55" y1="55" x2="59" y2="59"/>
            <line x1="31" y1="59" x2="35" y2="55"/><line x1="55" y1="35" x2="59" y2="31"/>
          </g>
        </svg>
        <div class="icon-label">12h</div>
      </div>
      <div class="icon-item">
        <svg viewBox="0 0 90 90" aria-label="BPA-frei">
          <circle cx="45" cy="45" r="40" fill="#f2f2f2" stroke="var(--ring-green)" stroke-width="6"/>
          <text x="45" y="53" text-anchor="middle" font-family="Exo 2, sans-serif" font-size="22" font-weight="700" fill="#333">BPA</text>
          <line x1="22" y1="22" x2="68" y2="68" stroke="var(--icon-grey)" stroke-width="7" opacity="0.8"/>
        </svg>
      </div>
    </div>

    <svg class="detail-connectors" viewBox="0 0 400 120" aria-hidden="true">
      <g fill="none" stroke="#ffffff" stroke-width="2">
        <polyline points="138,85 138,70 225,70 225,30"/>
        <polyline points="268,85 268,70 355,70 355,10"/>
      </g>
      <g fill="#ffffff">
        <polygon points="225,22 220,32 230,32"/>
        <polygon points="355,2 350,12 360,12"/>
      </g>
    </svg>
    <div class="detail-ring cap" role="img" aria-label="Detailfoto: Edelstahl-Deckel von oben"></div>
    <div class="detail-ring inside" role="img" aria-label="Detailfoto: doppelwandiger Querschnitt der Flasche"></div>

    <div class="product-title">
      <div class="thermo">THERMO</div>
      <div class="kind">Trinkflasche</div>
    </div>
    <p class="volume">500ML</p>
  </section>

</body>
</html>
```